Essential Oil Blend Label Design

I need a label designed for our stress relief essential blend, Marlow's Calm.
The text for the front of the logo will be as follows:
"Marlow's Calm
All Natural Stress and Anxiety Relief
www.brightmintcare.example"
Please make the front text small enough that it will show up in a picture of the bottle with the label is applied without being cut off on the edges. For reference, the label will be 4" x 2" and will go on these bottles:
http://www.vialcrafters.example/glass-bottles/european-dropper/amber/30ml-kvr30
On one of the sides of the label I would like this text, going up the label so that you turn the bottle sideways to read it (like in the attached label):
"Contains a pure, undiluted essential oil blend"
On the other side "For use in aromatherapy"
I would like this label to incorporate elements of a lush, green garden, like the Garden of Eden. The goal is for it convey peace and relaxation.
Please also note that I have attached the label for our other product for reference. The new label should be similar in its basic design as far as where the text is present and the overall style. My one problem with the attached label, though, is that the front text is a little too large and doesn't show up all the way in a picture. (I've attached the picture of the bottle as well so you can see what I mean).
I look forward to working with you!
Peter

```html
<!DOCTYPE html>
<html lang="en">
<head>
<meta charset="utf-8">
<title>Marlow's Calm – Essential Oil Blend Label</title>
<link rel="stylesheet" href="https://fonts.googleapis.com/css2?family=Crimson+Pro:ital,wght@0,400;0,500;0,700;1,700&display=swap">
<style>
  :root {
    --leaf-bright: #6cc545;
    --leaf-mid: #2f8a1c;
    --leaf-deep: #1c6410;
    --leaf-shadow: #154d0b;
    --band: rgba(14, 52, 8, 0.55);
    --title: #ffffff;
    --panel: #ffffff;
    --panel-text: #111111;
    --url: #f3ee3c;
  }
  * { margin: 0; padding: 0; box-sizing: border-box; }
  html, body {
    width: 1200px;
    height: 600px;
    overflow: hidden;
    background: #ffffff;
  }
  .label {
    position: relative;
    width: 1200px;
    height: 600px;
    overflow: hidden;
    font-family: "Crimson Pro", "Times New Roman", serif;
  }
  .foliage {
    position: absolute;
    inset: 0;
    background:
      radial-gradient(ellipse 75% 35% at 70% 0%, var(--leaf-bright) 0%, rgba(108,197,69,0) 100%),
      radial-gradient(ellipse 40% 30% at 8% 10%, var(--leaf-mid) 0%, rgba(47,138,28,0) 100%),
      linear-gradient(180deg, var(--leaf-mid) 0%, var(--leaf-deep) 45%, var(--leaf-deep) 75%, var(--leaf-shadow) 100%);
  }
  .footer-band {
    position: absolute;
    left: 0;
    right: 0;
    top: 503px;
    bottom: 0;
    background: var(--band);
  }
  .brand-name {
    position: absolute;
    top: 168px;
    left: 0;
    right: 0;
    text-align: center;
    color: var(--title);
    font-weight: 500;
    font-size: 66px;
    letter-spacing: 3px;
    line-height: 1;
    text-transform: uppercase;
  }
  .claim-panel {
    position: absolute;
    left: 310px;
    top: 270px;
    width: 570px;
    height: 110px;
    background: var(--panel);
    color: var(--panel-text);
    text-align: center;
    display: flex;
    flex-direction: column;
    justify-content: center;
    gap: 2px;
  }
  .claim-panel .benefit {
    font-size: 31px;
    font-weight: 400;
    line-height: 1.1;
  }
  .claim-panel .usage {
    font-size: 32px;
    font-weight: 700;
    font-style: italic;
    line-height: 1.1;
  }
  .website {
    position: absolute;
    top: 418px;
    left: 0;
    right: 0;
    text-align: center;
    color: var(--url);
    font-size: 37px;
    font-weight: 700;
    line-height: 1;
  }
</style>
</head>
<body>
  <main class="label">
    <div class="foliage" role="img" aria-label="Lush green ivy leaves covering the background, brightest along the top edge"></div>
    <div class="footer-band"></div>

    <h1 class="brand-name">Marlow’s Calm</h1>

    <div class="claim-panel">
      <p class="benefit">All Natural Stress &amp; Anxiety Relief</p>
      <p class="usage">For Use in Aromatherapy</p>
    </div>

    <p class="website">www.brightmintcare.example</p>
  </main>
</body>
</html>
```